Internet Of Things brochure

Need to create a brochure with a common theme to our website and the last 2 pages of the attached file. All the contect is in the file that I have attached.
website www.norvalegroup.com.au

Industry/Entity Type

Internet

```html
<!DOCTYPE html>
<html lang="en">
<head>
<meta charset="utf-8">
<title>Norvale Digital – Brochure</title>
<link href="https://fonts.googleapis.com/css2?family=Exo+2:ital,wght@0,300;0,400;0,500;0,600;1,300&display=swap" rel="stylesheet">
<style>
:root{
  --ink:#1e1e1e;
  --white:#ffffff;
  --band-grey:#d9d9db;
  --purple:#2e2553;
  --navy:#203a6c;
  --blue:#1e4b82;
  --soft:#e6e8f2;
}
*{margin:0;padding:0;box-sizing:border-box}
html,body{width:1200px;height:928px;overflow:hidden;background:var(--white)}
body{font-family:"Exo 2",sans-serif;font-weight:300;color:var(--ink);position:relative}
.page{position:absolute;top:0;height:928px;width:600px;overflow:hidden}
.page-left{left:0;background:var(--white)}
.page-right{left:600px;background:linear-gradient(180deg,var(--purple) 0%,#262f5e 30%,var(--navy) 52%,var(--blue) 100%);color:var(--white)}
.block{position:absolute}
h2{font-weight:500;font-size:15.5px;letter-spacing:.1px;line-height:1;text-transform:uppercase}
.lede{font-style:italic;font-size:10.4px;line-height:12.8px}
p{font-size:10.4px;line-height:12.8px;text-align:justify}
p+p{margin-top:12.8px}
.band{position:absolute;left:0;width:600px;background:var(--band-grey)}
.photo{position:absolute}
.intro-band{top:193px;height:242px}
.intro-band .photo{left:208px;top:0;width:392px;height:242px;background:linear-gradient(100deg,#b9bcc0 0%,#8d9196 40%,#c9b24a 75%,#e1c63a 100%)}
.intro-band .side-text{position:absolute;left:38px;top:10px;width:164px}
.questions-band{top:611px;height:203px}
.questions-band .photo{left:0;top:0;width:366px;height:203px;background:linear-gradient(135deg,#d2d3d5 0%,#9ea2a6 45%,#3b4c4e 70%,#c7c8ca 100%)}
.ask-box{position:absolute;left:366px;top:0;width:217px;height:203px;background:linear-gradient(180deg,var(--purple),#263a70);color:var(--white);padding:18px 16px 0 19px}
.ask-box h3{font-weight:400;font-size:10.4px;line-height:12.8px}
.ask-box p{font-style:italic;text-align:justify}
.ask-box p+p{margin-top:12.8px}
.scenarios h3{font-weight:500;font-size:12px;line-height:14px;margin-top:12px}
.scenarios p{font-style:italic}
.scenarios p b{font-style:normal;font-weight:500}
.helping{position:absolute;left:0;width:600px;top:265px;text-align:center;font-weight:500;font-size:15px}
.service-col{position:absolute;top:294px;width:240px}
.service-col h4{font-weight:400;font-size:12px;line-height:14.5px}
.service-col ul{list-style:none;margin-bottom:13px}
.service-col li{font-size:12px;line-height:14.5px;font-weight:300}
.service-col li::before{content:"· "}
.right-photo{left:0;top:480px;width:600px;height:229px;background:linear-gradient(120deg,#4b5666 0%,#7e8794 35%,#2d3644 60%,#8a94a2 85%,#5c6572 100%)}
</style>
</head>
<body>

<section class="page page-left">
  <div class="block" style="left:38px;top:42px;width:519px">
    <h2>Embrace digital or risk being left behind</h2>
    <div class="lede">Does your business have the Digital DNA required to succeed in the digital era?</div>
    <p style="margin-top:12.8px">Embracing the new revolution in digital technology is more than just having an eCommerce website - its about what is possible when every aspect of your business harnesses the power of digital innovation. When the sum of your business parts utilise digital and link together then your business can completely transform through being more effective, productive and automated.</p>
    <p>The way businesses operate has forever been changed by advancements in digital technology Integrated systems allow for sophisticated e-Commerce. automated business operations. digital marketing. CRMs and learning &amp; development opportunities.</p>
  </div>

  <div class="band intro-band">
    <div class="photo" role="img" aria-label="Technician using a tablet beside an industrial machine and yellow robotic arm"></div>
    <div class="side-text">
      <p>These can he connected together so that digital-ready businesses have never been more agile. nimble and ready to compete and serve. These elements combined amount to a serious threat to those who utilise a traditional business model and don t or can t adapt.</p>
      <p>Many enterprises have failed to adapt to this change. Through not integrating their business into the digital ecosystem. it exposes them to the possibility of failing to properly engage with their customers.</p>
    </div>
  </div>

  <div class="block" style="left:38px;top:455px;width:519px">
    <h2>The age of digital disruption is here</h2>
    <p>The world's largest taxi firm, Rydex, owns no vehicles. The world's largest accommodation provider. Staylo, owns no real estate. The world's biggest phone companies, Callwave and Chatterly, own no telco infrastructure. The world's most valuable retailer, Bazaarly, carries no stock. The most popular media company, Friendlink, creates no content. The world's largest movie house, Streamora, owns no cinemas. Something big has happened. It's called digital disruption.</p>
    <p>Creating and controlling the marketplace between the consumer and DIGITAL the provider of the goods or services is now the most valuable place to be. This is where risk is low. costs are slashed and profits are maximized.  This digital revolution poses both a significant threat and a significant  opportunity.</p>
  </div>

  <div class="band questions-band">
    <div class="photo" role="img" aria-label="Tablet showing a fleet management dashboard with map and KPI tiles"></div>
    <div class="ask-box">
      <h3>So ask yourself:</h3>
      <p>Is your business capable of responding quickly to digital threats?</p>
      <p>Are you doing all you can to compete in the digital business environment?</p>
      <p>Are you considering alternative business models and opportunities available through digitization?</p>
      <p>Does your business continue to grow in value in the face of digital threats?</p>
    </div>
  </div>

  <div class="block" style="left:38px;top:826px;width:519px">
    <p>Norvale Digital works closely with you to identify and focus on the valuable digital opportunities available to your business operation, re-design your processes and prepare your business for the task of competing in the global digital environment Partner with us and you'll discover what is possible for your business - and how you can take your business to another level.</p>
  </div>
</section>

<section class="page page-right">
  <div class="block scenarios" style="left:34px;top:42px;width:538px">
    <h2>Digital solutions</h2>
    <p style="font-style:normal;text-align:left">Our digital solutions are varied - impacting all parts of the business model and are completely tailored to your business and your industry.</p>
    <h3>We can cover the following scenarios (and more):</h3>
    <p><b>a)</b> Introduce a digitally strategic business model. digitising operations and processes by leveraging cloud-based applications and mobile devices that digitise data collection and collation and supply chain processes.</p>
    <p><b>b)</b> Learning &amp; Development solutions that comprise an array of digitised approaches that are always available on the Cloud. can be built in minutes. are completely customisable. are easy to maintain and are mobile friendly.</p>
    <p><b>c)</b> Seamlessly integrating digital commerce into your existing brick &amp;  mortar business quickly. strategically and cost effectively - helping you compete.</p>
    <p><b>d)</b> Creating targeted and measurable digital marketing campaigns that focus on increasing first-time and repeat sales and building long-term customer loyalty.</p>
  </div>

  <div class="helping">How we’re helping businesses reimagine their business through digital</div>

  <div class="service-col" style="left:83px">
    <h4>Digital Commerce</h4>
    <ul><li>eCommerce</li><li>mCommerce</li><li>Digital payment integration</li><li>Logistics and Supply Chain Integration</li></ul>
    <h4>Digital Marketing</h4>
    <ul><li>SEO &amp; SEM</li><li>Marketing Insights &amp; Analytics</li><li>Responsive EDMs and Digital Campaigns</li><li>Digital CTA</li><li>Proximity Marketing</li></ul>
  </div>
  <div class="service-col" style="left:342px">
    <h4>Digital Business Solutions</h4>
    <ul><li>Cloud ERP. CRM, SCM, HCM</li><li>IOT Integration to ERP. CRM. SCM</li><li>Digital invoicing solutions</li><li>Any device ERP. CRM, SCM</li></ul>
    <h4>Digital Learning</h4>
    <ul><li>Cloud LMS</li><li>Learning &amp; Development Solutions</li><li>Campus On Cloud</li></ul>
  </div>

  <div class="photo right-photo" role="img" aria-label="Hands holding a tablet showing a performance monitoring map dashboard in front of city buildings"></div>

  <div class="block" style="left:34px;top:724px;width:530px">
    <h2>Discovery workshop</h2>
    <p>The Digital Discovery Workshop is a half-day opportunity for the Key Stakeholders of your business that allows Norvale Digital to identify and explore which areas of your business are best suited to a digital transformation. During this  workshop you will also learn about the threats that the digital environment may pose to your business specifically. and the opportunities and possibilities that exist by applying digital solutions to your existing business.</p>
    <p>We also provide our clients with the opportunity to consider the overall strategy and actions needed within their organization to help them develop a competitive advantage inside the context of the ever-changing digital business environment. This analysis is relevant to all business types and industries.</p>
    <p style="font-style:italic">Interested in discovering your digital opportunities?</p>
  </div>
</section>

</body>
</html>
```